Chemical Distribution Company Needs a Website

We need a website designed for an existing company based in Michigan. We have grown substantially since inception and we need our website to reflect this growth. It currently has a very mom and pop feel to it. What we do is ship chemicals in Drums, Totes, Bags, Bulk Tank Trucks, and rail from our warehouses in Toledo Oh, and Chicago il. This will be a site that strictly shows what we do and will not be E-commerced based. The final design should communicate a large business with NorthAmerican reach and worldwide sourcing capabilities.

Target Market(s)

What we sell are chemicals such as acids, solvents, oils, and salts all of which are used in the manufacturing process of various products from steel to car parts to paint to car wash soaps to food. We are trying to look like a large company that has stability and track record to go after all types of industries and manufacturers

Industry/Entity Type

It Company

Number of Pages Required

5+ page

Font styles to use
Serif
Sans Serif

Requirements
Must have
• Be Formatted for WIX as that is what we use to Host and Build. Unless you have a better idea. I would also like it to be viewed on a mobile platform which it is not now.
• Tabs for:
• Home Page (similar to "www.brindlemoor.com")
• Who we are- with subtabs for (Overview, Leadership, and Capabilities)
• Chemicals- (subtabs for (overview, Chemicals A-Z) Look at Brindlemoor.com
• Metal Working Lubricants (with a drop down identical to the products tab at "www.veltraslube.com"
• Contact- Very similar to www.quorvanta.com/contact/
• Need to have professional photos of Chemical Facilities, Bulk Tanks Trucks, Chemical Railcars, Storage Facilities filled with Drums and Totes, a Tank Farm.
Nice to have
• Want to have our site look like a combination of quorvanta.com, brindlemoor.com, and plimtoreach.com

```html
<!DOCTYPE html>
<html lang="en">
<head>
<meta charset="utf-8">
<title>Korvane Chemicals</title>
<link rel="stylesheet" href="https://fonts.googleapis.com/css2?family=Aldrich&family=Lato:wght@400;700&display=swap">
<style>
:root{
  --navy:#0c4063;
  --navy-deep:#0a3450;
  --blue:#1e9be8;
  --text:#333b44;
  --muted:#8a9097;
  --line:#e3e6ea;
  --white:#ffffff;
  --head:"Aldrich",sans-serif;
  --body:"Lato",sans-serif;
}
*{box-sizing:border-box;margin:0;padding:0}
html,body{width:1200px;height:2628px;overflow:hidden}
body{position:relative;font-family:var(--body);color:var(--text);background:var(--white)}

/* header */
.site-header{position:absolute;left:0;top:0;width:1200px;height:114px;background:#f9fafb;border-bottom:1px solid var(--line)}
.brand{position:absolute;left:58px;top:24px;display:flex;align-items:center;gap:14px}
.brand-mark{width:58px;height:58px;border-radius:50%;background:var(--navy)}
.brand-name{font-family:var(--body);font-weight:700;font-size:30px;color:var(--navy);letter-spacing:1px}
.contact-item{position:absolute;top:36px;display:flex;gap:14px;align-items:flex-start}
.contact-item .label{color:var(--blue);font-size:16px;font-weight:700}
.contact-item .value{color:#5c636b;font-size:15px;margin-top:4px}

/* nav */
.main-nav{position:absolute;left:0;top:115px;width:1200px;height:75px;background:var(--white);border-bottom:1px solid var(--line)}
.main-nav ul{list-style:none;display:flex;position:absolute;left:34px;top:28px}
.main-nav li{font-size:14.5px;letter-spacing:.5px;color:#1d2a36;padding:0 37px;border-right:1px solid #c9ced3;line-height:18px}
.main-nav li:last-child{border-right:none}
.main-nav li.active{color:var(--blue)}
.search{position:absolute;left:960px;top:18px;width:196px;height:37px;border:1px solid #d7dbe0;display:flex}
.search span{flex:1;font-size:12px;color:#b4b9be;padding:11px 10px}
.search b{width:37px;background:var(--blue);display:flex;align-items:center;justify-content:center}

/* hero */
.hero{position:absolute;left:0;top:190px;width:1200px;height:610px;background:linear-gradient(180deg,#4a5866 0%,#6c7784 40%,#5a6a58 68%,#8d8a7e 100%)}
.hero-title{position:absolute;top:218px;width:1200px;text-align:center;font-family:var(--head);font-weight:400;font-size:46px;color:var(--white)}
.hero-text{position:absolute;top:293px;left:160px;width:880px;text-align:center;font-size:13.5px;line-height:22.5px;color:var(--white);font-weight:700}
.btn{display:inline-block;background:var(--blue);color:var(--white);font-size:13px;font-weight:700;text-align:center}
.hero .btn{position:absolute;left:513px;top:378px;width:133px;height:38px;line-height:38px}
.slide-arrow{position:absolute;top:248px;width:66px;height:66px;border-radius:50%;background:#e9eaec;display:flex;align-items:center;justify-content:center}

/* pillars */
.pillars{position:absolute;left:0;top:800px;width:1200px;height:234px;background:var(--navy)}
.pillars::before{content:"";position:absolute;left:0;top:0;width:1200px;height:2px;background:var(--white)}
.pillar{position:absolute;top:0;width:300px;text-align:center}
.pillar-icon{position:absolute;left:100px;top:-50px;width:100px;height:100px;border-radius:50%;border:2px solid var(--white);background:var(--navy);display:flex;align-items:center;justify-content:center}
.pillar-icon i{width:80px;height:80px;border-radius:50%;background:var(--white);display:flex;align-items:center;justify-content:center}
.pillar-icon.blue i{background:var(--blue)}
.pillar h3{position:absolute;top:69px;width:300px;font-family:var(--body);font-weight:400;font-size:20px;color:var(--white)}
.pillar p{position:absolute;top:105px;left:30px;width:240px;font-size:11px;line-height:17px;color:#e2eaf0}
.pillar .more{position:absolute;top:174px;width:300px;font-size:11px;font-weight:700;color:var(--white)}

/* chemicals */
.section-title{position:absolute;width:1200px;text-align:center;font-family:var(--head);font-weight:400;font-size:31px}
.chem-title{top:1082px;color:var(--blue)}
.chem-photo{position:absolute;left:67px;top:1160px;width:304px;height:263px;background:linear-gradient(135deg,#cfe9f8 0%,#7cc2ea 55%,#2f8fcf 100%)}
.chem-heading{position:absolute;left:408px;top:1154px;font-size:23px;font-weight:700;color:var(--navy)}
.chem-text{position:absolute;left:413px;top:1203px;width:722px;font-size:12.5px;line-height:28.5px;color:var(--muted);text-align:justify}
.chem-btn{position:absolute;left:413px;top:1386px;width:130px;height:37px;line-height:37px}

/* lubricants */
.lubes{position:absolute;left:0;top:1472px;width:1200px;height:310px;background:linear-gradient(180deg,#2a6a8e 0%,#1d5a7e 50%,#174c6c 100%)}
.lubes-title{top:46px;color:var(--white)}
.lube-col{position:absolute;top:135px;list-style:none}
.lube-col li{display:flex;align-items:center;gap:16px;color:var(--white);font-size:17px;height:40px}

/* social */
.follow-title{top:1820px;color:var(--navy)}
.follow-title span{color:var(--blue)}
.social{position:absolute;top:1906px;width:214px;text-align:center}
.social a{display:flex;align-items:center;justify-content:center;gap:14px;height:49px;color:var(--white);font-weight:700;font-size:20px;text-decoration:none}
.social a i{width:14px;height:14px;background:var(--white)}
.social small{display:block;margin-top:13px;font-size:13px;color:#7a8087}

/* get started */
.start{position:absolute;left:0;top:2027px;width:1200px;height:522px;background:linear-gradient(135deg,#3c4651 0%,#2b343d 50%,#242c34 100%)}
.start-title{position:absolute;left:67px;top:96px;font-family:var(--head);font-weight:400;font-size:26px;color:var(--white)}
.start-title span{color:var(--blue)}
.start-text{position:absolute;left:58px;top:147px;width:480px;font-size:11px;line-height:19px;color:var(--white)}
.start-rule{position:absolute;left:58px;top:226px;width:489px;height:1px;background:#cfd4d8}
.address{position:absolute;left:62px;top:252px;font-size:14px;line-height:28px;color:var(--white)}
.field{position:absolute;left:638px;width:487px;border:1px solid #c6cbd0;background:rgba(255,255,255,.08);color:var(--white);font-size:14px;padding:9px 14px}
.send{position:absolute;left:990px;top:447px;width:135px;height:40px;background:var(--white);color:var(--navy);font-size:17px;text-align:center;line-height:40px;letter-spacing:1px}

/* footer */
.site-footer{position:absolute;left:0;top:2549px;width:1200px;height:79px;background:var(--navy-deep)}
.site-footer p{position:absolute;left:48px;top:28px;font-size:12px;color:var(--white)}
.foot-icons{position:absolute;left:1003px;top:24px;display:flex;gap:10px}
.foot-icons i{width:28px;height:28px;border:1.5px solid var(--white)}
</style>
</head>
<body>

<header class="site-header">
  <div class="brand"><span class="brand-mark"></span><span class="brand-name">KORVANE CHEMICALS</span></div>
  <div class="contact-item" style="left:648px">
    <svg width="40" height="30" viewBox="0 0 40 30"><path d="M2 10 L28 2 L36 24 L10 30 Z" fill="#0c4063"/><path d="M2 10 L22 18 L28 2" stroke="#fff" stroke-width="1.5" fill="none"/></svg>
    <div><div class="label">Email id :</div><div class="value">hello@korvanechem.com</div></div>
  </div>
  <div class="contact-item" style="left:1018px">
    <svg width="20" height="24" viewBox="0 0 20 24"><path d="M4 2 L8 2 L10 8 L7 10 Q9 15 13 17 L15 14 L20 17 L19 22 Q10 22 5 14 Q1 8 4 2Z" fill="#0c4063"/></svg>
    <div><div class="label">Call Us :</div><div class="value">08 4417 2603</div></div>
  </div>
</header>

<nav class="main-nav">
  <ul>
    <li class="active">HOME</li>
    <li>WHO WE ARE</li>
    <li>CHEMICALS</li>
    <li>METAL WORKING LUBRICANTS</li>
    <li>CONTACT</li>
  </ul>
  <div class="search"><span>Search</span><b><svg width="14" height="14" viewBox="0 0 14 14"><circle cx="6" cy="6" r="4" stroke="#fff" stroke-width="2" fill="none"/><path d="M9 9 L13 13" stroke="#fff" stroke-width="2"/></svg></b></div>
</nav>

<section class="hero" role="img" aria-label="Photo of a green bulk tank truck hauling a white trailer on a desert highway">
  <h1 class="hero-title">LOREM IPSUM DOLOR SIT AMET</h1>
  <p class="hero-text">Lorem ipsum dolor sit amet, consectetur adipiscing elit, sed do eiusmod tempor incididunt ut labore et dolore magna aliqua.<br>Ut enim ad minim veniam, quis nostrud exercitation ullamco laboris nisi ut aliquip ex ea commodo consequat. Duis aute irure<br>dolor in reprehenderit in voluptate velit esse cillum dolore eu fugiat nulla pariatur.</p>
  <span class="btn">READ MORE</span>
  <span class="slide-arrow" style="left:-12px"><svg width="12" height="16" viewBox="0 0 12 16"><path d="M9 2 L3 8 L9 14" stroke="#222" stroke-width="2.5" fill="none"/></svg></span>
  <span class="slide-arrow" style="left:1158px"><svg width="12" height="16" viewBox="0 0 12 16"><path d="M3 2 L9 8 L3 14" stroke="#222" stroke-width="2.5" fill="none"/></svg></span>
</section>

<section class="pillars">
  <div class="pillar" style="left:104px">
    <div class="pillar-icon"><i><svg width="44" height="36" viewBox="0 0 44 36"><circle cx="22" cy="9" r="7" fill="#1e9be8"/><circle cx="9" cy="13" r="5" fill="#1e9be8"/><circle cx="35" cy="13" r="5" fill="#1e9be8"/><path d="M10 36 Q10 19 22 19 Q34 19 34 36Z" fill="#1e9be8"/><path d="M0 34 Q0 21 9 21 Q12 21 13 23 Q8 27 8 34Z M44 34 Q44 21 35 21 Q32 21 31 23 Q36 27 36 34Z" fill="#1e9be8"/></svg></i></div>
    <h3>LEADERSHIP</h3>
    <p>Lorem ipsum dolor sit amet, consectetur adipiscing elit, sed do eiusmod tempor incididunt ut labore et dolore magna aliqua.</p>
    <div class="more">MORE &#9656;</div>
  </div>
  <div class="pillar" style="left:447px">
    <div class="pillar-icon blue"><i><svg width="40" height="40" viewBox="0 0 40 40"><path d="M8 4 H26 L32 10 V36 H8Z" fill="none" stroke="#fff" stroke-width="2.5"/><path d="M13 14 H24 M13 20 H20" stroke="#fff" stroke-width="2"/><circle cx="24" cy="26" r="6" fill="none" stroke="#fff" stroke-width="2.5"/><path d="M28 30 L34 36" stroke="#fff" stroke-width="3"/></svg></i></div>
    <h3>OVERVIEW</h3>
    <p>Lorem ipsum dolor sit amet, consectetur adipiscing elit, sed do eiusmod tempor incididunt ut labore et dolore magna aliqua. Ut</p>
    <div class="more">MORE &#9656;</div>
  </div>
  <div class="pillar" style="left:784px">
    <div class="pillar-icon blue"><i><svg width="44" height="40" viewBox="0 0 44 40"><circle cx="17" cy="22" r="11" fill="none" stroke="#fff" stroke-width="6" stroke-dasharray="4 3"/><circle cx="17" cy="22" r="5" fill="#fff"/><circle cx="33" cy="10" r="6" fill="none" stroke="#fff" stroke-width="4" stroke-dasharray="3 2"/><circle cx="35" cy="30" r="5" fill="none" stroke="#fff" stroke-width="4" stroke-dasharray="3 2"/></svg></i></div>
    <h3>CAPABILITIES</h3>
    <p>Lorem ipsum dolor sit amet, consectetur adipiscing elit, sed do eiusmod tempor incididunt ut labore et dolore magna aliqua.</p>
    <div class="more">MORE &#9656;</div>
  </div>
</section>

<h2 class="section-title chem-title">CHEMICALS</h2>
<div class="chem-photo" role="img" aria-label="Photo of laboratory glassware and a molecule model in blue light"></div>
<h3 class="chem-heading">Commodity, Specialty and Custom formulas</h3>
<p class="chem-text">Lorem ipsum dolor sit amet, consectetur adipiscing elit, sed do eiusmod tempor incididunt ut labore et dolore magna aliqua. Ut enim ad minim veniam, quis nostrud exercitation ullamco laboris nisi ut aliquip ex ea commodo consequat. Duis aute irure dolor in reprehenderit in voluptate velit esse cillum dolore eu fugiat nulla pariatur. Excepteur sint occaecat cupidatat non proident, sunt in culpa qui officia deserunt mollit anim id est laborum. Laboris nisi ut aliquip ex ea commodo consequat. Duis aute irure dolor in reprehenderit in voluptate velit esse cillum dolore eu fugiat nulla pariatur. Excepteur sint occaecat cupidatat non proident, sunt in culpa qui officia deserunt mollit anim id est laborum.</p>
<span class="btn chem-btn">READ MORE</span>

<section class="lubes" role="img" aria-label="Photo of metal machining with coolant spray, tinted blue">
  <h2 class="section-title lubes-title">METAL WORKING LUBRICANTS</h2>
  <ul class="lube-col" style="left:163px">
    <li><svg width="16" height="12"><path d="M1 6 L6 11 L15 1" stroke="#1e9be8" stroke-width="3" fill="none"/></svg>Vanishing</li>
    <li><svg width="16" height="12"><path d="M1 6 L6 11 L15 1" stroke="#1e9be8" stroke-width="3" fill="none"/></svg>Machining &amp; Cutting</li>
    <li><svg width="16" height="12"><path d="M1 6 L6 11 L15 1" stroke="#1e9be8" stroke-width="3" fill="none"/></svg>Honing</li>
  </ul>
  <ul class="lube-col" style="left:485px;top:133px">
    <li><svg width="16" height="12"><path d="M1 6 L6 11 L15 1" stroke="#1e9be8" stroke-width="3" fill="none"/></svg>Gun Drill</li>
    <li><svg width="16" height="12"><path d="M1 6 L6 11 L15 1" stroke="#1e9be8" stroke-width="3" fill="none"/></svg>Grinding</li>
    <li><svg width="16" height="12"><path d="M1 6 L6 11 L15 1" stroke="#1e9be8" stroke-width="3" fill="none"/></svg>Extrusion &amp; Cold Heading</li>
  </ul>
  <ul class="lube-col" style="left:816px;top:133px">
    <li><svg width="16" height="12"><path d="M1 6 L6 11 L15 1" stroke="#1e9be8" stroke-width="3" fill="none"/></svg>Drawing &amp; Stamping</li>
    <li><svg width="16" height="12"><path d="M1 6 L6 11 L15 1" stroke="#1e9be8" stroke-width="3" fill="none"/></svg>Transmission oils</li>
    <li><svg width="16" height="12"><path d="M1 6 L6 11 L15 1" stroke="#1e9be8" stroke-width="3" fill="none"/></svg>Tractor oils</li>
  </ul>
</section>

<h2 class="section-title follow-title"><span>FOLLOW US</span> TO STAY IN TOUCH</h2>
<div class="social" style="left:89px"><a style="background:#1a6ecf"><i></i>Friendlane</a><small>1234 Like</small></div>
<div class="social" style="left:368px"><a style="background:#1ea6e6"><i></i>Chirpline</a><small>1234 Followers</small></div>
<div class="social" style="left:639px"><a style="background:#1b4e66"><i></i>Workgrid</a><small>1234 Followers</small></div>
<div class="social" style="left:904px"><a style="background:#c8203a"><i></i>Snapframe</a><small>1234 Followers</small></div>

<section class="start" role="img" aria-label="Dark map of North America behind the contact form">
  <h2 class="start-title"><span>GET</span> STARTED</h2>
  <p class="start-text">Lorem ipsum dolor sit amet, consectetur adipiscing elit, sed do eiusmod tempor incididunt ut labore et dolore magna aliqua. Ut enim ad minim veniam, quis nostrud exercitation ullamco laboris nisi ut aliquip ex ea commodo consequat.</p>
  <div class="start-rule"></div>
  <div class="address">123 Address line1, Address line 2<br>Country, 123456.<br>Freephone: +1 234 567 890<br>Telephone: +1 234 567 890<br>FAX: +1 234 567 899<br><span style="display:block;margin-top:30px">E-mail: mail@korvanechem.com</span></div>
  <div class="field" style="top:149px;height:37px">Name</div>
  <div class="field" style="top:216px;height:35px">Email id</div>
  <div class="field" style="top:282px;height:35px">Phone</div>
  <div class="field" style="top:343px;height:83px">Address</div>
  <div class="send">SEND</div>
</section>

<footer class="site-footer">
  <p>Copyright 2016 Company Name. All Rights Reserved.</p>
  <div class="foot-icons"><i></i><i></i><i></i><i></i></div>
</footer>

</body>
</html>
```